Website Templates Design Project

BrawnLoop Template Websites
Creative Brief

BrawnLoop Gyms
The growth of BrawnLoop Gyms (or boxes, as they are called by members) is an amazing world-wide phenomenon. More than 3,400 gyms ranging from “garage gyms” to massive retail locations have opened in recent years. The philosophy for workouts at the gym is built around is “constantly varied (if not random), high intensity, functional movement". Each gym does what is called a WOD, or Workout of the Day. Workouts are typically short—20 minutes or less—and intense, demanding all-out physical exertion.
The growth of the gyms, mainly in the United States, has generally come from military veterans, police officers and fireman. However, BrawnLoop box owners are mostly trainers and not necessarily skilled in operating or marketing a business. Our company is launching a new platform for boxes to purchase inexpensive template websites and other marketing materials.
The Need
Most BrawnLoop box owners have launched with basic WordPress websites. We see an opportunity to provide more dynamic and professional websites, using a template and content management system. We aim to offer multiple template designs (not WordPress) for box owners. The platform that we are using can be found at www.sitekitpreview7.com. We are looking for graphic designs that will fit this platform.
A big part of the BrawnLoop philosophy is built around an Internet-based community. Therefore, our website templates should allow for a robust blog that allows for posting of pictures and video by members and the box owner.
The Designs
We strongly encourage designers to review other BrawnLoop websites for design ideas and functionality (good and bad).
We are looking for cutting-edge designs. One person on our team said, “these sites need to be so good that they sweat!” Obviously, imagery that portrays working out and muscles will be attractive to box owners. Many of the graphics for BrawnLoop sites use particularly masculine images like diamond plate and steel. The designs should be contemporary and at first glance you show know that this is a BrawnLoop website.
Rotating images and video windows are good, just nothing that will require long load times.

Images and Logos
Please don’t pirate logos ad images from BrawnLoop sites without permission. For your design submissions, feel free to develop generic logos and names for BrawnLoop Gyms. If you use and stock photography, please indicate whether you have permission to use or where permission can be obtained.

The navigation for a basic website design (and your designs) should include:
Home (with WOD blog dominating body of page)
About Us
Store
Membership Info (with link to store)
Directions
Contact Us

Target Market(s)

18-35, athletic types, male and female

Industry/Entity Type

Marketing

Requirements
Must have
• Navigation "buttons":

About Us
Store
Directions
Contact Us

```html
<!DOCTYPE html>
<html lang="en">
<head>
<meta charset="utf-8">
<title>BrawnLoop Gyms</title>
<link rel="stylesheet" href="https://fonts.googleapis.com/css2?family=Noto+Sans:wght@400;700&display=swap">
<style>
:root{
  --page:#041a1e;
  --header-top:#3d5358;
  --header-bot:#22373c;
  --band:#0c2a30;
  --panel:#0a2a31;
  --panel-line:#1f4a52;
  --footer:#021417;
  --text-light:#d6dedf;
  --text-mid:#a9b7b9;
  --text-dim:#6f8a8e;
  --teal-text:#3f8c99;
  --accent:#1f6e82;
  --accent-dark:#0f4656;
  --input:#d8dde0;
}
*{box-sizing:border-box;margin:0;padding:0}
html,body{width:1200px;height:943px;overflow:hidden}
body{background:var(--page);font-family:"Noto Sans",Verdana,sans-serif;color:var(--text-light);position:relative}
.abs{position:absolute}

.site-header{left:0;top:0;width:1200px;height:67px;background:linear-gradient(180deg,var(--header-top),var(--header-bot));border-bottom:1px solid #101e21}
.brand{left:218px;top:20px;font-size:24px;font-weight:700;color:#c9d3d5;letter-spacing:.5px}
.main-nav a{position:absolute;top:32px;height:26px;line-height:26px;font-size:13px;color:var(--text-light);text-decoration:none}
.main-nav a.current{background:linear-gradient(180deg,#2f8aa1,var(--accent-dark));border:1px solid #5fa9bb;border-radius:4px;padding:0 12px}

.hero{left:0;top:67px;width:1200px;height:326px;background:radial-gradient(ellipse 420px 330px at 600px 170px,#5d6c70 0%,#33403f 45%,#0b0e0e 80%,#000 100%)}
.hero-dots{left:960px;top:367px;display:flex;gap:4px}
.hero-dots span{width:13px;height:13px;border-radius:50%;background:#c9cfd1}
.hero-dots span.active{background:var(--accent)}

.band{left:0;top:393px;width:1200px;height:440px;background:linear-gradient(180deg,#16363c 0%,var(--band) 45%,#08242a 100%);border-top:1px solid #2a4c52}
.band-rule{left:0;top:617px;width:1200px;height:1px;background:#1d4148}

.login{left:215px;top:406px;width:228px;height:166px;background:rgba(12,48,58,.85);border:1px solid #3d6a74;border-radius:6px}
.login h2{position:absolute;left:0;top:10px;width:100%;text-align:center;font-size:18px;font-weight:400;color:var(--text-mid)}
.login .rule{position:absolute;left:0;top:40px;width:100%;height:1px;background:#3d6a74}
.login label{position:absolute;left:11px;font-size:11px;color:var(--text-light)}
.login .field{position:absolute;height:22px;background:var(--input);border:1px solid #9aa8ab}
.login .forgot{position:absolute;left:11px;top:135px;font-size:12px;color:var(--text-mid)}
.login .btn-login{position:absolute;left:156px;top:131px;width:58px;height:23px;line-height:21px;text-align:center;font-size:11px;color:var(--text-light);border:1px solid #4c7d88;background:#0e3540}

.welcome h1{left:460px;top:416px;font-size:21px;font-weight:400;color:var(--text-mid)}
.welcome .rule{left:460px;top:448px;width:578px;height:2px;background:#6a8489}
.welcome p{left:460px;top:461px;width:572px;font-size:13.5px;line-height:20.5px;color:#6e8488;text-align:justify}

.btn-more{position:absolute;height:21px;line-height:21px;text-align:center;font-size:10px;color:var(--text-light);background:linear-gradient(180deg,#2a7489,var(--accent-dark));border-radius:3px;box-shadow:0 1px 2px #000}

.content{left:215px;top:578px;width:823px;height:247px;background:rgba(8,40,48,.75);box-shadow:0 2px 6px rgba(0,0,0,.5)}
.section-title{position:absolute;top:10px;font-size:14px;font-weight:700;color:var(--text-mid)}
.divider{left:269px;top:52px;width:1px;height:183px;background:#1b434a}

.member-photo{left:35px;top:52px;width:70px;height:98px;background:linear-gradient(180deg,#c7d3d8,#32508a 70%,#22304a);border:2px solid #8ea4aa}
.member-info{left:114px;top:52px;font-size:10px;line-height:21px;color:var(--teal-text)}
.member-note{left:35px;top:160px;width:215px;font-size:10.5px;line-height:15.7px;color:var(--teal-text);text-align:justify}
.member-note b{color:var(--text-light)}

.post{position:absolute;top:52px;width:237px}
.post h3{font-size:10.5px;font-weight:700;color:var(--text-light);display:flex;justify-content:space-between}
.post h3 time{font-weight:400;font-size:9.5px}
.post p{margin-top:2px;font-size:10.5px;line-height:15.5px;color:var(--teal-text);text-align:justify}

.site-footer{left:0;top:833px;width:1200px;height:110px;background:var(--footer)}
.footer-nav a{position:absolute;top:28px;font-size:12px;color:var(--text-light);text-decoration:none}
.footer-nav a.current{text-decoration:underline}
.copyright{left:0;top:48px;width:1200px;text-align:center;font-size:12px;color:var(--text-light)}
.copyright em{font-weight:700;text-decoration:underline}
</style>
</head>
<body>

<header class="site-header abs">
  <div class="brand abs">BrawnLoop Gyms</div>
  <nav class="main-nav">
    <a class="current" href="#" style="left:655px">Home</a>
    <a href="#" style="left:724px">About Us</a>
    <a href="#" style="left:809px">Store</a>
    <a href="#" style="left:871px">Directions</a>
    <a href="#" style="left:952px">Contact Us</a>
  </nav>
</header>

<div class="hero abs" role="img" aria-label="Rotating banner photo of a smiling female athlete flexing and a muscular male athlete against a dark steel wall"></div>
<div class="hero-dots abs"><span></span><span class="active"></span><span></span></div>

<div class="band abs"></div>
<div class="band-rule abs"></div>

<form class="login abs">
  <h2>Member Login</h2>
  <div class="rule"></div>
  <label style="top:62px">E-mail &nbsp;&nbsp;&nbsp;:</label>
  <div class="field" style="left:73px;top:59px;width:142px"></div>
  <label style="top:96px">Password :</label>
  <div class="field" style="left:75px;top:93px;width:142px"></div>
  <span class="forgot">Forget Password?</span>
  <span class="btn-login">Login</span>
</form>

<section class="welcome">
  <h1 class="abs">Welcome To Our Site</h1>
  <div class="rule abs"></div>
  <p class="abs">Lorem Ipsum is simply dummy text of the printing and typesetting industry. Lorem Ipsum has been the industry's standard dummy text ever since the 1500s, when an unknown printer took a galley of type and scrambled it to make a type specimen book.</p>
  <span class="btn-more" style="left:960px;top:547px;width:70px">Read More</span>
</section>

<section class="content abs">
  <h2 class="section-title" style="left:34px">Membership Info</h2>
  <h2 class="section-title" style="left:290px">Our Blog</h2>
  <div class="divider abs"></div>

  <div class="member-photo abs" role="img" aria-label="Member portrait photo"></div>
  <div class="member-info abs">
    Name : Rex Calder<br>Age : 35 yrs old<br>Weight : 70 Kg.<br>Mob : 12345678<br>Mem. Till : 12.12.2010
  </div>
  <p class="member-note abs"><b>Lorem Ipsum</b> is simply dummy text of the printing and typesetting industry. Lorem&nbsp; dummy text ever.</p>
  <span class="btn-more" style="left:178px;top:216px;width:69px">Read More</span>

  <article class="post" style="left:289px">
    <h3><span>Headline goes here</span><time>31 Aug, 2011</time></h3>
    <p>Lorem Ipsum is simply dummy text of the printing and typesetting industry. Lorem Ipsum has been the industry's standard dummy text everindustry. Lorem Ipsum is simply dummy text of the printing and typesetting industry. Lorem Ipsum has been the industry's everindustry. Lorem Ipsum has been the industry's everindustry. Lorem Ipsum has been the industry's everindustry.</p>
  </article>
  <article class="post" style="left:554px">
    <h3><span>Headline goes here</span><time>31 Aug, 2011</time></h3>
    <p>Lorem Ipsum is simply dummy text of the printing and typesetting industry. Lorem Ipsum has been the industry's standard dummy text everindustry. Lorem Ipsum is simply dummy text of the printing and typesetting industry. Lorem Ipsum has been the industry's everindustry. Lorem Ipsum has been the industry's everindustry. Lorem Ipsum has been the industry's everindustry.</p>
  </article>
  <span class="btn-more" style="left:721px;top:216px;width:70px">Read More</span>
</section>

<footer class="site-footer abs">
  <nav class="footer-nav">
    <a class="current" href="#" style="left:478px">Home</a>
    <a href="#" style="left:530px">About Us</a>
    <a href="#" style="left:608px">Store</a>
    <a href="#" style="left:679px">Directions</a>
    <a href="#" style="left:754px">Contact Us</a>
  </nav>
  <p class="copyright abs">@ copyright, <em>BrawnLoopGyms</em></p>
</footer>

</body>
</html>
```